Stationery Design for Pfotenhaus

We already have a logo a Logo for our outstanding veterinary hospital. Now we are looking for our future letterhead, business cards and envelopes. We would like to see a design using the color from our logo. Additional color should be limited to grey or a rusty brown. The font should be easy and clearly readable and must be easily available on all computers (to install it in our Management software). The finial design should communicate competence in veterinary medicine, and empathy.

To meet the European regulation (DIN5008) there are a couple mandatory legal informations one the letterhead. We also enclosed a template of exact measurement, which need to be respected according to DIN5008.

Mandatory legal information are (best placed in the footer):
"Pfotenhaus GmbH & Co KG, Brunnfeldgasse 417C, 1140 Wien,
Handelsgericht Wien, FN 294617k, GF: Dr. Lorenz Haidinger
ATU 3918462"
Additional informations needed:
"Tel: +43 1 5849162, Fax: +43 1 5849163, info@pfotenhaus-demo.at, www. pfotenhaus-demo.at"
bank account informations should be included as well. These are:
"Sparkasse Hollental Nord, IBAN: AT 58 1111 2222 3333 4444, BIC: HLNTAT2H517"

The Logo should be in the upper right corner. Below that we need a space for informations regarding the responsible veterinarians. There will be 3-5 Names, each of it consisting of 2 lines (see example below). The Names should be highlighted (larger font) compared to the qualifications in the second line.
Tierärztliche Leitung:
Dr. Lorenz Haidinger
Diplomate ECVS
Updates

The contest was startet on the 2nd of may and the deadline was a day later? Why was that so fast? Did I do something wrong? BR

Target Market(s)

dog and cat owner in Austria as welle as referring veterinarians in Austria

Industry/Entity Type

Veterinary

Contact Information for Business Card

One side: Logo
other side:
Dr. Lorenz Haidinger
Diplomate ECVS
EBVS Specialist of Small Animal Surgery

Pfotenhaus GmbH&Co KG
Brunnfeldgasse 417C
1140 Wien

Tel: +43 1 5849160 DW 102
Fax: +43 1 5849160 DW 999
email: lorenz.haidinger@pfotenhaus-demo.at

Font styles to use
Serif
Sans Serif

Requirements
Must have
• The logo should be given in the upper right. Most of the legal informations should be given in the footer. The upper left Area should be clear, since the recipient address will be placed there.
Colors should be limited to golden, blue and greyscale (two different gereysacales at most).

```html
<!DOCTYPE html>
<html lang="de">
<head>
<meta charset="utf-8">
<title>Pfotenhaus – Briefpapier</title>
<link href="https://fonts.googleapis.com/css2?family=Montserrat:wght@600&family=Source+Sans+3:wght@400;600;700&display=swap" rel="stylesheet">
<style>
  :root {
    --navy: #1a2a57;
    --gold: #d9ab2a;
    --orange: #f7941d;
    --ink: #111111;
    --paper: #ffffff;
    --stage: #ffffff;
  }
  * { margin: 0; padding: 0; box-sizing: border-box; }
  html, body { width: 893px; height: 1200px; overflow: hidden; background: var(--stage); }
  body { position: relative; font-family: "Source Sans 3", sans-serif; color: var(--navy); }

  .presentation-title {
    position: absolute; left: 0; width: 893px; top: 26px;
    text-align: center; font-family: "Montserrat", sans-serif; font-weight: 600;
    font-size: 27px; letter-spacing: 2.5px; color: var(--orange); line-height: 32px;
  }
  .presentation-subtitle {
    position: absolute; left: 0; width: 893px; top: 74px;
    text-align: center; font-family: "Montserrat", sans-serif; font-weight: 600;
    font-size: 21px; letter-spacing: 1.5px; color: var(--ink); line-height: 26px;
  }

  .sheet {
    position: absolute; left: 96px; top: 146px; width: 705px; height: 1001px;
    background: var(--paper);
    box-shadow: 0 0 6px rgba(0,0,0,0.25);
    overflow: hidden;
  }

  .brand { position: absolute; left: 425px; top: 13px; display: flex; align-items: center; }
  .brand-dot { width: 70px; height: 70px; border-radius: 50%; background: var(--navy); flex: none; }
  .brand-name {
    margin-left: 6px; font-weight: 700; font-size: 29px; color: var(--navy);
    letter-spacing: 0.3px; line-height: 1;
  }

  .board-heading {
    position: absolute; left: 425px; top: 87px;
    font-weight: 600; font-size: 12px; line-height: 14px; color: var(--navy);
  }
  .board-rule {
    position: absolute; left: 537px; right: 0; top: 98px; height: 1.5px; background: var(--navy);
  }
  .board {
    position: absolute; left: 425px; top: 112px; width: 270px;
    display: grid; grid-template-columns: 90px 90px 90px; row-gap: 3px;
  }
  .vet-name { font-weight: 600; font-size: 9px; line-height: 12px; color: var(--gold); white-space: nowrap; }
  .vet-title { font-size: 6.5px; line-height: 10px; color: var(--navy); }

  .recipient { position: absolute; left: 88px; top: 173px; }
  .recipient-label { font-size: 9px; line-height: 11px; color: var(--navy); }
  .recipient-name { font-weight: 600; font-size: 12px; line-height: 16px; color: var(--navy); }

  .footer {
    position: absolute; left: 0; bottom: 0; width: 705px; height: 103px;
    background: var(--gold); color: var(--paper);
    text-align: center; font-size: 11px; padding-top: 14px;
  }
  .footer p { line-height: 14.5px; }
  .footer .gap { margin-top: 4px; }
  .footer strong { font-weight: 700; }
</style>
</head>
<body>
  <h1 class="presentation-title">LETTERHEAD DESIGN MOCKUP- 1</h1>
  <h2 class="presentation-subtitle">WITHOUT CONTENT</h2>

  <main class="sheet">
    <div class="brand">
      <span class="brand-dot"></span>
      <span class="brand-name">Pfotenhaus</span>
    </div>

    <div class="board-heading">Tierärztliche Leitung:</div>
    <div class="board-rule"></div>
    <div class="board">
      <div class="vet"><div class="vet-name">Dr. Lorenz Haidinger</div><div class="vet-title">Diplomate ECVS</div></div>
      <div class="vet"><div class="vet-name">Dr. Lorenz Haidinger</div><div class="vet-title">Diplomate ECVS</div></div>
      <div class="vet"><div class="vet-name">Dr. Lorenz Haidinger</div><div class="vet-title">Diplomate ECVS</div></div>
      <div class="vet"><div class="vet-name">Dr. Lorenz Haidinger</div><div class="vet-title">Diplomate ECVS</div></div>
      <div class="vet"><div class="vet-name">Dr. Lorenz Haidinger</div><div class="vet-title">Diplomate ECVS</div></div>
    </div>

    <div class="recipient">
      <div class="recipient-label">To</div>
      <div class="recipient-name">Jonas Berger</div>
    </div>

    <footer class="footer">
      <p>Pfotenhaus GmbH &amp; Co KG, Brunnfeldgasse 417C, 1140 Wien, Handelsgericht Wien, FN 294617kx,</p>
      <p>GF: <strong>Dr. Lorenz Haidinger ATU 3918462</strong></p>
      <p class="gap"><strong>Tel:</strong> +43 1 5849162, <strong>Fax:</strong> +43 1 5849163, <strong>E-Mail:</strong> info@pfotenhaus-demo.at <strong>Website:</strong> www. pfotenhaus-demo.at</p>
      <p><strong>Sparkasse Hollental Nord, IBAN:</strong> AT 58 1111 2222 3333 4444, <strong>BIC:</strong> HLNTAT2H517</p>
    </footer>
  </main>
</body>
</html>
```